Business Card Design and stationary (thank you cards)

I am basically starting a "handyman" business but have a little ego issue with that term. I have been a professional in the design and construction business for 30 years. I want simple…I will define the scope of work I do as i move forward, and it can vary and i want it to vary.

Target Market(s)

Homeowners mostly

Industry/Entity Type

Business

Contact Information for Business Card

Company Name is "Tidy Corner Crew" Dale P. Whitcombe, 42 Larkvale Hollow Road, Alderbrook, Vt, 06419 (but I may want to use a PO Box), Phone is 555-555-0187, email is dwhitcombe584@mailnest.example,

Font styles to use
Sans Serif

Requirements
Should not have
• anything pre designed….hammers or whatever…custom lines to make home features as shone but simple and elegant

```html
<!DOCTYPE html>
<html lang="en">
<head>
<meta charset="utf-8">
<title>Tidy Corner Crew – Business Card</title>
<link rel="stylesheet" href="https://fonts.googleapis.com/css2?family=Open+Sans:wght@400;600;700;800&display=swap">
<style>
  :root {
    --brand-blue: #0a52a0;
    --brand-yellow: #f2c40f;
    --logo-blue: #1b8ccb;
    --ink: #1a1a1a;
    --paper: #fbfbfa;
    --backdrop: #d9d9d7;
  }
  * { box-sizing: border-box; margin: 0; padding: 0; }
  html, body {
    width: 1200px; height: 1000px; overflow: hidden;
    background: var(--backdrop);
    font-family: "Open Sans", Arial, sans-serif;
  }
  .card {
    position: absolute; left: 210px;
    width: 780px; height: 446px;
    background: var(--paper);
    overflow: hidden;
    box-shadow: 0 2px 6px rgba(0,0,0,.12);
  }
  .card--front { top: 36px; }
  .card--back { top: 518px; }
  .card__bands { position: absolute; inset: 0; }

  .wordmark {
    position: absolute;
    color: var(--logo-blue);
    font-weight: 800;
    text-transform: uppercase;
    line-height: 1.05;
    text-align: center;
  }
  .card--front .wordmark { left: 330px; top: 92px; width: 260px; font-size: 46px; }
  .card--back .wordmark { left: 536px; top: 112px; width: 190px; font-size: 33px; }

  .name-pill {
    position: absolute; left: 78px; top: 96px;
    width: 300px; height: 54px;
    background: var(--brand-blue);
    border-radius: 0 27px 27px 0;
    color: #fff; font-weight: 700; font-size: 21px;
    display: flex; align-items: center; padding-left: 34px;
  }
  .contact-list {
    position: absolute; left: 26px; top: 188px;
    list-style: none; color: var(--ink); font-size: 19px;
  }
  .contact-list li { display: flex; align-items: center; height: 34px; gap: 10px; white-space: nowrap; }
  .contact-list svg { width: 20px; height: 20px; flex: none; }
</style>
</head>
<body>

<section class="card card--front" aria-label="Card front">
  <svg class="card__bands" viewBox="0 0 780 446" aria-hidden="true">
    <rect x="0" y="0" width="780" height="12" fill="var(--brand-blue)"/>
    <path d="M300 12 H780 V48 H360 Q320 48 300 12 Z" fill="var(--brand-yellow)"/>
    <path d="M0 316 L560 336 L560 342 L0 322 Z" fill="var(--brand-yellow)"/>
    <path d="M0 336 L540 356 Q600 358 640 330 Q670 312 720 314 L780 316 V446 H0 Z" fill="var(--brand-blue)"/>
  </svg>
  <div class="wordmark">Tidy<br>Corner<br>Crew</div>
</section>

<section class="card card--back" aria-label="Card back">
  <svg class="card__bands" viewBox="0 0 780 446" aria-hidden="true">
    <rect x="0" y="78" width="24" height="72" fill="var(--brand-yellow)"/>
    <path d="M378 123 H500 L520 150 H536" fill="none" stroke="var(--brand-blue)" stroke-width="5"/>
    <path d="M536 150 V100 H720 V200" fill="none" stroke="var(--brand-blue)" stroke-width="5"/>
    <path d="M536 190 V262 H722 V212 H770" fill="none" stroke="var(--brand-yellow)" stroke-width="5"/>
    <path d="M0 300 L560 328 L560 340 L0 314 Z" fill="var(--brand-yellow)"/>
    <path d="M0 326 L540 352 Q600 354 640 326 Q670 308 720 310 L780 312 V446 H0 Z" fill="var(--brand-blue)"/>
    <circle cx="52" cy="104" r="9" fill="var(--ink)"/>
    <path d="M34 140 Q34 116 52 116 Q70 116 70 140 Z" fill="var(--ink)"/>
    <path d="M50 117 L54 117 L53 132 L51 132 Z" fill="#fff"/>
  </svg>

  <div class="name-pill">Dale P. Whitcombe</div>

  <ul class="contact-list">
    <li>
      <svg viewBox="0 0 24 24" aria-hidden="true"><path d="M6 3 L10 3 L11 8 L8 10 Q10 14 14 16 L16 13 L21 14 L21 18 Q21 21 18 21 Q4 20 3 6 Q3 3 6 3 Z" fill="var(--ink)"/></svg>
      <span>: 555-555-0187</span>
    </li>
    <li>
      <svg viewBox="0 0 24 24" aria-hidden="true"><rect x="2" y="5" width="20" height="14" fill="var(--ink)"/><path d="M2 5 L12 13 L22 5" fill="none" stroke="#fff" stroke-width="1.6"/></svg>
      <span>: dwhitcombe584@mailnest.example</span>
    </li>
    <li>
      <svg viewBox="0 0 24 24" aria-hidden="true"><path d="M12 2 Q6 2 6 8 Q6 12 12 18 Q18 12 18 8 Q18 2 12 2 Z" fill="none" stroke="var(--ink)" stroke-width="2"/><circle cx="12" cy="8" r="2.4" fill="var(--ink)"/><path d="M3 21 H21" stroke="var(--ink)" stroke-width="2"/></svg>
      <span>: 42 Larkvale Hollow Road, Alderbrook, Vt, 06419</span>
    </li>
  </ul>

  <div class="wordmark">Tidy<br>Corner<br>Crew</div>
</section>

</body>
</html>
```